Task Description: Full Vehicle Wrap Design for Stone Heron – Rodent & Exclusion Company
We’re launching a design contest for a full vehicle wrap for Stone Heron, our rodent control and exclusion company. We’re looking for a design that is bold, clean, and communicates what we do — while also standing out on the road.

About the Company
Before you start designing, please visit our website: www.StoneHeronUSA.com. Learn what we do and how we serve homeowners. Understanding our mission will help your design align with our brand and services.

Vehicles in Our Fleet
We're looking for wraps that will be consistent across multiple vehicles in our fleet:

16-foot Box Truck

Side Panels: 16 ft wide x 8 ft tall

Back Door: 8 ft wide x 8 ft tall

Note: The back of the truck is critical — it’s what drivers behind us see most, so that space must clearly and simply convey our service and name.

2016 Brenk Tavora Pell Cargo XL

Please look up this model online for reference.

Smaller van, perfect for mobile service calls. Needs a complementary design to the box truck.

2020 Brenk Q-420 XL

Optional third vehicle. A clean, scaled-down version of the box truck or van design would be ideal for consistency.

Design Direction
We’ve uploaded a file with three visual examples of directions we like. Please review all three and choose the one that resonates most with your artistic style. Don’t try to blend all three — we want to see how your creativity builds on the one you connect with most.

The goal is:

Brand recognition

Clear messaging (what we do, who we are)

Clean, modern, eye-catching — not cluttered

Ideally: something that can be extended or scaled across the different vehicle sizes

```html
<!DOCTYPE html>
<html lang="en">
<head>
<meta charset="utf-8">
<title>Stone Heron – Fleet Wrap Panels</title>
<link href="https://fonts.googleapis.com/css2?family=Oswald:wght@300;500&family=Poppins:wght@500;600;700;800&display=swap" rel="stylesheet">
<style>
  :root {
    --orange: #e8661f;
    --amber: #f39a1e;
    --charcoal: #262626;
    --ink: #1b1b1b;
    --white: #ffffff;
    --body-white: #f4f4f4;
    --outline: #d6d6d6;
  }
  * { margin: 0; padding: 0; box-sizing: border-box; }
  html, body { width: 1200px; height: 1200px; overflow: hidden; background: var(--white); }
  body { position: relative; font-family: "Poppins", sans-serif; }

  .vehicle-side { position: absolute; left: 100px; width: 1000px; }
  .vehicle-side--box { top: 70px; height: 330px; }
  .vehicle-side--van { top: 470px; height: 250px; }
  .vehicle-side--pickup { top: 820px; height: 250px; }
  .side-art { position: absolute; inset: 0; width: 100%; height: 100%; }

  /* shared wrap block, base size 900 x 300 */
  .wrap-block {
    position: absolute; width: 900px; height: 300px;
    transform-origin: top left; overflow: hidden;
    background: var(--charcoal); color: var(--white);
  }
  .vehicle-side--box .wrap-block { left: 0; top: 0; transform: scale(1.1111, 1.1); }
  .vehicle-side--van .wrap-block { left: 420px; top: 30px; transform: scale(0.6); background: transparent; }
  .vehicle-side--pickup .wrap-block { left: 400px; top: 40px; transform: scale(0.56); background: transparent; }

  .wrap-block__arc { position: absolute; right: 0; top: 0; width: 200px; height: 240px; }

  .brand { position: absolute; left: 30px; top: 18px; display: flex; align-items: center; gap: 18px; }
  .brand__dot { width: 54px; height: 54px; border-radius: 50%; background: var(--orange); }
  .brand__name {
    font-family: "Oswald", sans-serif; font-weight: 300; font-size: 66px;
    color: var(--amber); letter-spacing: 2px; line-height: 1;
  }

  .tagline { position: absolute; left: 30px; top: 96px; font-size: 15px; font-weight: 700; }
  .tagline em { font-style: normal; color: var(--orange); }

  .offer {
    position: absolute; left: 30px; top: 128px; background: var(--orange);
    font-weight: 800; font-size: 21px; padding: 1px 10px; letter-spacing: 1px;
  }
  .phone { position: absolute; left: 30px; top: 160px; font-weight: 700; font-size: 34px; letter-spacing: 1px; }

  .rodent-mark {
    position: absolute; left: 500px; top: 110px; width: 96px; height: 96px; border-radius: 50%;
    background: radial-gradient(circle, #7a5a42 0%, #5b4130 45%, var(--orange) 47%);
  }

  .promise { position: absolute; right: 18px; top: 112px; width: 90px; text-align: center; }
  .promise__icons { display: flex; justify-content: center; gap: 6px; margin-bottom: 6px; }
  .promise__icons span { width: 18px; height: 18px; border-radius: 50%; border: 2px solid var(--white); }
  .promise__text { font-size: 11px; font-weight: 800; line-height: 1.15; }

  .cta {
    position: absolute; left: 0; top: 208px; width: 100%; height: 38px; background: var(--ink);
    font-weight: 600; font-size: 27px; line-height: 38px; padding-left: 30px;
  }
  .benefits {
    position: absolute; left: 0; top: 252px; width: 100%; height: 48px; background: var(--orange);
    display: flex; align-items: center; justify-content: space-between; padding: 0 30px;
    font-size: 10px; font-weight: 700; text-transform: uppercase;
  }
  .benefit { display: flex; align-items: center; gap: 8px; }
  .benefit__tick {
    width: 14px; height: 14px; border: 1.5px solid var(--white); border-radius: 2px;
    display: flex; align-items: center; justify-content: center;
  }
  .vehicle-side--van .cta, .vehicle-side--pickup .cta { width: 820px; }
  .vehicle-side--van .benefits, .vehicle-side--pickup .benefits { background: transparent; top: 246px; }
</style>
</head>
<body>

<!-- Box truck side -->
<section class="vehicle-side vehicle-side--box">
  <div class="wrap-block">
    <svg class="wrap-block__arc" viewBox="0 0 200 240" aria-hidden="true">
      <path d="M70 0 Q150 100 110 240 L200 240 L200 0 Z" fill="#e8661f"/>
      <path d="M40 0 Q120 100 96 240 L110 240 Q150 100 70 0 Z" fill="#f39a1e"/>
    </svg>
    <div class="brand"><span class="brand__dot"></span><span class="brand__name">STONE HERON</span></div>
    <p class="tagline">Specializes in <em>rat control</em>, <em>mice control</em>, and <em>rodent-proofing</em></p>
    <p class="offer">FREE INSPECTION</p>
    <p class="phone">510-555-0142</p>
    <div class="rodent-mark" role="img" aria-label="Rat photo inside a no-entry circle"></div>
    <div class="promise">
      <div class="promise__icons"><span></span><span></span><span></span></div>
      <p class="promise__text">Remove them<br>FOR GOOD!</p>
    </div>
    <p class="cta">Protect your home. Get started today!</p>
    <div class="benefits">
      <span class="benefit"><span class="benefit__tick">✓</span>Absolutely no poisons or toxic chemicals</span>
      <span class="benefit"><span class="benefit__tick">✓</span>One-time treatment</span>
      <span class="benefit"><span class="benefit__tick">✓</span>Locally owned &amp; operated</span>
    </div>
  </div>
</section>

<!-- Cargo van side -->
<section class="vehicle-side vehicle-side--van">
  <svg class="side-art" viewBox="0 0 1000 250" aria-hidden="true">
    <rect x="1" y="1" width="998" height="248" rx="24" fill="#f4f4f4" stroke="#d6d6d6"/>
    <path d="M260 0 L975 0 Q1000 0 1000 24 L1000 226 Q1000 250 975 250 L360 250 Q300 130 260 0 Z" fill="#e8661f"/>
    <path d="M260 0 L760 0 Q800 70 790 130 L330 130 Q290 70 260 0 Z" fill="#262626"/>
    <path d="M740 0 Q800 60 785 130 L800 130 Q815 60 760 0 Z" fill="#f39a1e"/>
    <circle cx="310" cy="170" r="110" fill="#262626"/>
    <rect x="420" y="162" width="500" height="24" fill="#1b1b1b"/>
  </svg>
  <div class="wrap-block">
    <div class="brand"><span class="brand__dot"></span><span class="brand__name">STONE HERON</span></div>
    <p class="tagline">Specializes in <em>rat control</em>, <em>mice control</em>, and <em>rodent-proofing</em></p>
    <p class="offer">FREE INSPECTION</p>
    <p class="phone">510-555-0142</p>
    <div class="rodent-mark" role="img" aria-label="Rat photo inside a no-entry circle"></div>
    <div class="promise">
      <div class="promise__icons"><span></span><span></span><span></span></div>
      <p class="promise__text">Remove them<br>FOR GOOD!</p>
    </div>
    <p class="cta">Protect your home. Get started today!</p>
    <div class="benefits">
      <span class="benefit"><span class="benefit__tick">✓</span>Absolutely no poisons or toxic chemicals</span>
      <span class="benefit"><span class="benefit__tick">✓</span>One-time treatment</span>
      <span class="benefit"><span class="benefit__tick">✓</span>Locally owned &amp; operated</span>
    </div>
  </div>
</section>

<!-- Pickup side -->
<section class="vehicle-side vehicle-side--pickup">
  <svg class="side-art" viewBox="0 0 1000 250" aria-hidden="true">
    <rect x="1" y="1" width="998" height="248" rx="20" fill="#f4f4f4" stroke="#d6d6d6"/>
    <path d="M300 20 L980 20 Q1000 20 1000 40 L1000 230 Q1000 250 980 250 L360 250 Q310 140 300 20 Z" fill="#e8661f"/>
    <path d="M330 30 L730 30 Q760 90 750 150 L360 150 Q335 90 330 30 Z" fill="#262626"/>
    <path d="M700 30 Q760 90 745 150 L760 150 Q775 90 720 30 Z" fill="#f39a1e"/>
    <circle cx="300" cy="175" r="100" fill="#262626"/>
    <rect x="400" y="163" width="460" height="22" fill="#1b1b1b"/>
  </svg>
  <div class="wrap-block">
    <div class="brand"><span class="brand__dot"></span><span class="brand__name">STONE HERON</span></div>
    <p class="tagline">Specializes in <em>rat control</em>, <em>mice control</em>, and <em>rodent-proofing</em></p>
    <p class="offer">FREE INSPECTION</p>
    <p class="phone">510-555-0142</p>
    <div class="rodent-mark" role="img" aria-label="Rat photo inside a no-entry circle"></div>
    <div class="promise">
      <div class="promise__icons"><span></span><span></span><span></span></div>
      <p class="promise__text">Remove them<br>FOR GOOD!</p>
    </div>
    <p class="cta">Protect your home. Get started today!</p>
    <div class="benefits">
      <span class="benefit"><span class="benefit__tick">✓</span>Absolutely no poisons or toxic chemicals</span>
      <span class="benefit"><span class="benefit__tick">✓</span>One-time treatment</span>
      <span class="benefit"><span class="benefit__tick">✓</span>Locally owned &amp; operated</span>
    </div>
  </div>
</section>

</body>
</html>
```